Bluewater Products Flyer

Bluewater Lending Group, Inc.
Licensed Mortgage Company
Serving the DMV since 1997
"You choose Bluewater, we'll carry it home"
We specialize in...
FHA Loans
* Credit Scores as low as 500
* 203K Renovation Loans
Conventional Loans
* As little as 1% Down
* Bank Statement for Self-Employed
Investor Loans
* DSCR, & Fix & Flip
* Commercial & New Construction
Other Programs
* HELOCS & Reverse Mortgages
Call today for a free consultation
(800) 641-2957
www.bluewaterlendhub.com
NMLS #731846

```html
<!DOCTYPE html>
<html lang="en">
<head>
<meta charset="utf-8">
<title>Bluewater Products Flyer</title>
<link href="https://fonts.googleapis.com/css2?family=Libre+Baskerville:wght@700&family=Poppins:wght@400;500;600;700;800&display=swap" rel="stylesheet">
<style>
  :root {
    --navy: #173d6e;
    --navy-deep: #12325c;
    --gold: #e3c06b;
    --gold-dark: #b8902f;
    --gold-light: #f3dc96;
    --red: #d0313f;
    --white: #ffffff;
    --page: #ffffff;
  }
  * { margin: 0; padding: 0; box-sizing: border-box; }
  html, body { width: 1064px; height: 1200px; overflow: hidden; background: var(--page); }
  body { font-family: "Poppins", sans-serif; color: var(--navy); }
  .flyer { position: relative; width: 1064px; height: 1200px; background: var(--white); overflow: hidden; }

  .brand { position: absolute; left: 52px; top: 58px; width: 330px; text-align: center; }
  .brand-mark { width: 44px; height: 44px; border-radius: 50%; background: var(--gold); margin: 0 auto 10px; }
  .brand-name { font-weight: 700; font-size: 20px; line-height: 1.2; color: var(--navy); white-space: nowrap; }
  .brand-tag { font-size: 10px; font-weight: 500; margin-top: 6px; color: var(--navy); }
  .brand-est { font-size: 11px; font-weight: 600; letter-spacing: 2px; margin-top: 3px; color: var(--navy); }

  .headline { position: absolute; left: 62px; top: 242px; width: 460px; }
  .headline .lead { font-family: "Libre Baskerville", serif; font-weight: 700; font-size: 42px; letter-spacing: -1px; color: var(--navy-deep); line-height: 1.1; white-space: nowrap; }
  .headline .big { font-family: "Libre Baskerville", serif; font-weight: 700; font-size: 52px; letter-spacing: -1.5px; line-height: 1.25; margin-top: 18px; white-space: nowrap;
    background: linear-gradient(90deg, var(--gold-dark), var(--navy) 30%, var(--navy-deep)); -webkit-background-clip: text; background-clip: text; color: transparent; }
  .headline .tail { font-weight: 700; font-size: 29px; color: var(--navy-deep); margin-top: 22px; letter-spacing: 0.3px; white-space: nowrap; }

  .hero { position: absolute; left: 542px; top: 45px; width: 522px; height: 430px; }

  .specialize-tab { position: absolute; left: 60px; top: 533px; width: 477px; height: 57px; z-index: 2;
    background: linear-gradient(90deg, var(--gold), var(--gold-light) 60%, var(--gold));
    clip-path: polygon(0 0, 100% 0, 96% 100%, 0 100%);
    font-weight: 800; font-size: 41px; color: var(--navy-deep); line-height: 57px; padding-left: 12px; }

  .products { position: absolute; left: 0; top: 570px; width: 1064px; height: 395px; background: var(--navy); }
  .product { position: absolute; }
  .product .icon { position: absolute; left: 0; top: 0; width: 124px; height: 124px; }
  .product .info { position: absolute; top: 6px; width: 320px; }
  .product h3 { font-weight: 700; font-size: 29px; line-height: 1.1; color: var(--gold); letter-spacing: 0.3px; }
  .product ul { list-style: none; margin-top: 10px; }
  .product li { position: relative; padding-left: 19px; font-size: 18px; line-height: 1.3; color: var(--white); }
  .product li::before { content: ""; position: absolute; left: 2px; top: 8px; width: 10px; height: 10px; border-radius: 50%; background: var(--white); }
  .product li::after { content: ""; position: absolute; left: 5px; top: 10px; width: 3px; height: 5px; border: solid var(--navy); border-width: 0 1.5px 1.5px 0; transform: rotate(45deg); }

  .fha { left: 60px; top: 50px; } .fha .info { left: 170px; top: 12px; }
  .investor { left: 592px; top: 50px; } .investor .info { left: 170px; top: 8px; }
  .conventional { left: 62px; top: 213px; } .conventional .info { left: 170px; top: 8px; }
  .other { left: 592px; top: 213px; } .other .info { left: 170px; top: 8px; }

  .cta-ribbon { position: absolute; left: 0; top: 978px; width: 500px; height: 100px; }
  .cta-text { position: absolute; left: 62px; top: 1002px; font-weight: 600; font-size: 30px; line-height: 1.12; color: var(--white); }

  .phone { position: absolute; left: 530px; top: 1005px; display: flex; align-items: center; gap: 12px; }
  .phone-num { font-weight: 700; font-size: 53px; color: var(--navy-deep); letter-spacing: 0.5px; }

  .footer-bar { position: absolute; left: 0; top: 1095px; width: 1064px; height: 58px; background: var(--gold);
    display: flex; align-items: center; }
  .web { padding-left: 62px; padding-right: 24px; font-size: 35px; font-weight: 500; color: var(--navy-deep); white-space: nowrap; }
  .divider { width: 2px; height: 40px; background: var(--white); }
  .web b { font-weight: 700; }
  .nmls { padding-left: 44px; font-size: 31px; font-weight: 500; color: var(--navy-deep); white-space: nowrap; }
  .nmls b { font-weight: 700; }
</style>
</head>
<body>
<main class="flyer">
  <header class="brand">
    <div class="brand-mark"></div>
    <div class="brand-name">Bluewater Lending Group, Inc.</div>
    <div class="brand-tag">YOU CHOOSE BLUEWATER, WE'LL CARRY IT HOME.</div>
    <div class="brand-est">EST. 1997</div>
  </header>

  <section class="headline">
    <div class="lead">YOU CHOOSE</div>
    <div class="big">BLUEWATER</div>
    <div class="tail">WE'LL CARRY IT HOME</div>
  </section>

  <svg class="hero" viewBox="0 0 522 430">
    <defs>
      <linearGradient id="frameGold" x1="0" y1="0" x2="0" y2="1">
        <stop offset="0" stop-color="#f2d98e"/>
        <stop offset="1" stop-color="#b88f2f"/>
      </linearGradient>
      <linearGradient id="photoTone" x1="0" y1="0" x2="1" y2="1">
        <stop offset="0" stop-color="#f1eeea"/>
        <stop offset="0.5" stop-color="#a6735a"/>
        <stop offset="1" stop-color="#e8e2dc"/>
      </linearGradient>
    </defs>
    <polygon points="261,0 522,175 522,430 0,430 0,170" fill="url(#frameGold)"/>
    <polygon points="261,24 502,187 502,412 20,412 20,183" fill="#ffffff"/>
    <polygon points="20,183 80,140 442,140 502,187 502,412 20,412" fill="url(#photoTone)" role="img" aria-label="Photo of a smiling family of four sitting together at home"/>
  </svg>

  <div class="specialize-tab">WE SPECIALIZE IN</div>

  <section class="products">
    <div class="product fha">
      <svg class="icon" viewBox="0 0 124 124"><circle cx="62" cy="62" r="58" fill="none" stroke="#fff" stroke-width="4"/>
        <path d="M40 50 L62 36 L84 50 Z" fill="#fff"/><rect x="44" y="52" width="36" height="20" fill="none" stroke="#fff" stroke-width="4"/>
        <line x1="62" y1="36" x2="62" y2="22" stroke="#fff" stroke-width="3"/><path d="M62 22 L74 26 L62 30 Z" fill="#fff"/>
        <path d="M28 84 L50 80 L72 84 L92 72 L96 78 L74 94 L28 94 Z" fill="#fff"/>
        <text x="62" y="70" text-anchor="middle" font-family="Poppins, sans-serif" font-weight="700" font-size="16" fill="#fff">$</text></svg>
      <div class="info"><h3>FHA LOANS</h3>
        <ul><li>Credit Scores as low as 500</li><li>203K Renovation Loans</li></ul></div>
    </div>

    <div class="product investor">
      <svg class="icon" viewBox="0 0 124 124"><circle cx="62" cy="62" r="58" fill="none" stroke="#fff" stroke-width="4"/>
        <circle cx="74" cy="38" r="15" fill="none" stroke="#fff" stroke-width="4"/>
        <text x="74" y="44" text-anchor="middle" font-family="Poppins, sans-serif" font-weight="700" font-size="16" fill="#fff">$</text>
        <rect x="58" y="56" width="32" height="8" rx="4" fill="#fff"/><rect x="58" y="67" width="32" height="8" rx="4" fill="#fff"/>
        <rect x="24" y="76" width="12" height="22" fill="#fff"/><path d="M40 80 L60 80 L92 72 L96 78 L70 94 L40 94 Z" fill="#fff"/></svg>
      <div class="info"><h3>INVESTOR<br>LOANS</h3>
        <ul><li>DSCR, &amp; Fix &amp; Flip</li><li>Commercial &amp; New<br>Construction</li></ul></div>
    </div>

    <div class="product conventional">
      <svg class="icon" viewBox="0 0 124 124"><circle cx="62" cy="62" r="58" fill="none" stroke="#fff" stroke-width="4"/>
        <path d="M44 40 L62 26 L80 40" fill="none" stroke="#fff" stroke-width="4"/>
        <rect x="40" y="46" width="44" height="26" rx="3" fill="#fff"/>
        <text x="62" y="66" text-anchor="middle" font-family="Poppins, sans-serif" font-weight="700" font-size="18" fill="#173d6e">$</text>
        <rect x="24" y="80" width="12" height="22" fill="#fff"/><path d="M40 84 L60 84 L92 76 L96 82 L70 98 L40 98 Z" fill="#fff"/></svg>
      <div class="info"><h3>CONVENTIONAL<br>LOANS</h3>
        <ul><li>As little as 1% Down</li><li>Bank Statement for<br>Self-Employed</li></ul></div>
    </div>

    <div class="product other">
      <svg class="icon" viewBox="0 0 124 124"><circle cx="62" cy="62" r="58" fill="none" stroke="#fff" stroke-width="4"/>
        <path d="M26 56 L58 30 L90 56" fill="none" stroke="#fff" stroke-width="5"/>
        <path d="M34 52 L34 92 L66 92 L66 64 L82 64 L82 52" fill="none" stroke="#fff" stroke-width="4"/>
        <circle cx="76" cy="76" r="10" fill="#fff"/><circle cx="96" cy="84" r="12" fill="#fff"/>
        <text x="76" y="81" text-anchor="middle" font-family="Poppins, sans-serif" font-weight="700" font-size="13" fill="#173d6e">$</text>
        <text x="96" y="90" text-anchor="middle" font-family="Poppins, sans-serif" font-weight="700" font-size="15" fill="#173d6e">$</text></svg>
      <div class="info"><h3>OTHER<br>PROGRAMS</h3>
        <ul><li>HELOCS</li><li>Reverse Mortgages</li></ul></div>
    </div>
  </section>

  <svg class="cta-ribbon" viewBox="0 0 500 100">
    <path d="M0 22 L440 22 Q466 18 492 0 Q500 30 478 60 Q455 90 420 94 L0 94 Z" fill="#d0313f"/>
    <path d="M492 0 Q480 40 440 60 Q460 40 440 22 Q466 18 492 0 Z" fill="#a8222e"/>
  </svg>
  <div class="cta-text">Call today for a<br>Free consultation</div>

  <div class="phone">
    <svg width="40" height="40" viewBox="0 0 40 40"><circle cx="20" cy="20" r="19" fill="#c9a24a"/>
      <path d="M13 11 L17 11 L19 16 L16 18 Q18 23 22 24 L24 21 L29 23 L29 27 Q28 30 24 29 Q13 26 11 15 Q11 11 13 11 Z" fill="#fff"/></svg>
    <span class="phone-num">(800) 641-2957</span>
  </div>

  <footer class="footer-bar">
    <div class="web">www.<b>bluewaterlendhub</b>.com</div>
    <div class="divider"></div>
    <div class="nmls">NMLS <b>#731846</b></div>
  </footer>
</main>
</body>
</html>
```